Travel Poster Design Project

A poster design for a specific Adventure Travel Journey to Ladakh India. The journey it will be promoting is a 2 week trekking and cultural tour through Ladakh passing over 2 mountain passes in excess of 5000 meters.

Dates are July and August each year

Brand Name is Far Ridge Voyages

We do inspiring unique journeys in a small select number of locations around the world. Ladakh is also known as Little Tibet and has a buddhist culture

We have a logo already to use and we also have a range of photos online for you to select from. They can be seen at http://photos.brookcanoe.example/FarRidgeVoyages then click on Ladakh

Target Market(s)

Adventure travel people 30-55 poster will be displayed in our rafting retail base so will be seen by target market

Industry/Entity Type

Travel

Requirements
Must have
• website address www.farridgevoyages.example
Phone Number 01632 960418
email info@farridgevoyages.example
Pictures
small legal note along the bottom, saying Far Ridge Voyages is a brand name of Torrent Bend Paddle Outfitters LLP
Nice to have
• Lots of inspiring photos and colour
Should not have
• named dates

```html
<!DOCTYPE html>
<html lang="en">
<head>
<meta charset="utf-8">
<title>Ladakh India – Travel Journey</title>
<link rel="stylesheet" href="https://fonts.googleapis.com/css2?family=Cormorant+Garamond:wght@400;500&family=Tinos&display=swap">
<style>
  :root {
    --band-blue: #4066dc;
    --title-yellow: #f4ec8c;
    --date-yellow: #f2e68a;
    --text-white: #ffffff;
    --frame-white: #fbfbfb;
    --brand-navy: #1f3170;
    --sky-top: #f1f2f4;
    --sky-mid: #b9bcc4;
    --rock-low: #5c6270;
    --rock-deep: #3d4350;
  }
  * { margin: 0; padding: 0; box-sizing: border-box; }
  html, body { width: 800px; height: 1200px; overflow: hidden; background: #ffffff; }
  .poster {
    position: relative;
    width: 800px;
    height: 1200px;
    overflow: hidden;
    font-family: "Cormorant Garamond", Georgia, serif;
    font-variant-numeric: lining-nums;
  }
  .backdrop {
    position: absolute; inset: 0;
    background:
      radial-gradient(ellipse 70% 30% at 50% 22%, rgba(255,255,255,0.85), rgba(255,255,255,0) 70%),
      linear-gradient(180deg, var(--sky-top) 0%, #d9dbe0 25%, var(--sky-mid) 48%, #8d93a0 62%, var(--rock-low) 80%, var(--rock-deep) 100%);
  }
  .top-band {
    position: absolute; left: 0; top: 0; width: 800px; height: 75px;
    background: var(--band-blue);
    border-bottom: 2px solid #c9cfe0;
  }
  .place-name {
    position: absolute; left: 18px; top: 10px;
    font-size: 54px; font-weight: 500; line-height: 1;
    color: var(--title-yellow);
  }
  .journey-title {
    position: absolute; left: 0; width: 800px; top: 125px;
    text-align: center;
    font-size: 86px; font-weight: 400; line-height: 1;
    color: var(--text-white);
    text-shadow: 0 0 6px rgba(120,120,130,0.5);
  }
  .snapshot {
    position: absolute;
    background: var(--frame-white);
    padding: 14px;
    box-shadow: 2px 4px 10px rgba(0,0,0,0.35);
  }
  .snapshot .photo { width: 100%; height: 100%; }
  .snapshot--palace { left: 14px; top: 398px; width: 308px; height: 306px; transform: rotate(-8deg); z-index: 1; }
  .snapshot--stupa  { left: 258px; top: 270px; width: 290px; height: 290px; transform: rotate(5deg); z-index: 2; }
  .snapshot--rock   { left: 458px; top: 390px; width: 318px; height: 300px; transform: rotate(8deg); z-index: 3; }
  .photo--palace { background: linear-gradient(180deg, #4e8fe0 0%, #a9c8ee 38%, #e4e0d6 55%, #9a8672 80%, #5c6a3e 100%); }
  .photo--stupa  { background: linear-gradient(180deg, #5d9be6 0%, #b9d3f1 30%, #c9b79a 52%, #8c6d4e 80%, #b6a587 100%); }
  .photo--rock   { background: linear-gradient(160deg, #8e8a80 0%, #b7b1a4 35%, #6e7a5a 60%, #a09684 100%); }
  .season {
    position: absolute; left: 330px; top: 702px;
    font-size: 42px; font-weight: 500; line-height: 1;
    color: var(--date-yellow);
  }
  .contact {
    position: absolute; left: 385px; top: 766px;
    font-style: normal;
    font-size: 27px; line-height: 38px;
    color: var(--text-white);
  }
  .contact .contact-line { display: block; white-space: nowrap; }
  .brand-mark {
    position: absolute; left: 403px; top: 896px; width: 374px; height: 128px;
    background: #ffffff;
    display: flex; align-items: center; justify-content: center; gap: 14px;
  }
  .brand-mark .dot { width: 34px; height: 34px; border-radius: 50%; background: var(--brand-navy); }
  .brand-mark .brand-name {
    font-size: 40px; font-weight: 500; color: var(--brand-navy); line-height: 1;
  }
  .highlights {
    position: absolute; left: 12px; top: 780px; list-style: none;
    color: var(--text-white);
    font-size: 38px; line-height: 58px;
  }
  .highlights li { position: relative; padding-left: 38px; margin-bottom: 14px; }
  .highlights li::before {
    content: ""; position: absolute; left: 4px; top: 22px;
    width: 18px; height: 18px; border-radius: 50%; background: var(--text-white);
  }
  .highlights .line { display: block; }
  .highlights li:nth-child(2) { line-height: 46px; padding-top: 6px; }
  .highlights li:nth-child(2)::before { top: 20px; }
  .bottom-band {
    position: absolute; left: 0; bottom: 0; width: 800px; height: 69px;
    background: var(--band-blue);
  }
  .legal-note {
    position: absolute; left: 403px; top: 7px; width: 390px;
    font-family: "Tinos", "Times New Roman", serif;
    font-size: 18.5px; line-height: 25px; color: var(--text-white);
  }
  .legal-note .line { display: block; white-space: nowrap; }
</style>
</head>
<body>
<main class="poster">
  <div class="backdrop" role="img" aria-label="Misty snow-streaked Himalayan mountain range under a pale cloudy sky"></div>

  <header class="top-band">
    <h1 class="place-name">Ladakh India</h1>
  </header>

  <h2 class="journey-title">Travel Journey</h2>

  <figure class="snapshot snapshot--palace">
    <div class="photo photo--palace" role="img" aria-label="White domed building with balconies against a blue sky in Leh"></div>
  </figure>
  <figure class="snapshot snapshot--stupa">
    <div class="photo photo--stupa" role="img" aria-label="Buddhist stupa gateway with painted red and gold trim"></div>
  </figure>
  <figure class="snapshot snapshot--rock">
    <div class="photo photo--rock" role="img" aria-label="Buddha painting carved on a rocky cliff face with prayer wheels"></div>
  </figure>

  <p class="season">July and August each year</p>

  <address class="contact">
    <span class="contact-line">Phone:&nbsp; 01632 960418</span>
    <span class="contact-line">email: info@farridgevoyages.example</span>
    <span class="contact-line">web: www.farridgevoyages.example</span>
  </address>

  <div class="brand-mark">
    <span class="dot"></span>
    <span class="brand-name">Far Ridge Voyages</span>
  </div>

  <ul class="highlights">
    <li><span class="line">2 weeks of</span><span class="line">trekking and</span><span class="line">cultural tour</span></li>
    <li><span class="line">2x 5000+ meters</span><span class="line">mountain passes</span></li>
  </ul>

  <footer class="bottom-band">
    <p class="legal-note"><span class="line">Far Ridge Voyages is a brand name of</span><span class="line">Torrent Bend Paddle Outfitters LLP</span></p>
  </footer>
</main>
</body>
</html>
```